Marlowe Hairdressing Business Card Design

The design has to be based upon a colour scheme of a black gloss background and silver type face letters and has to portray an exclusive and expensive outlet.

The business card has a dual use with the rear of the card being used for future appointments therefore this area has to be lined out to accept written text.

We also need to incorporate a Chatterbook log somewhere on the card.

Target Market(s)

High Earning individuals with high disposable incomes possible link too young professionals.

Contact Information for Business Card

Marlowe Hairdressing & The Willowmere Beauty
Tel 01632 418550
www.marlowehairdressing.example.co.uk

Requirements
Must have
• Company Name including beauty element, telephone number, website and chatterbook please.
Nice to have
• High Gloss finish with silver raised letters or similar
Should not have
• Hairdressing Images like, scissors, haircuts, beauty treatments etc

```html
<!DOCTYPE html>
<html lang="en">
<head>
<meta charset="utf-8">
<title>Marlowe Hairdressing &amp; The Willowmere Beauty — Business Card</title>
<link rel="stylesheet" href="https://fonts.googleapis.com/css2?family=Pirata+One&family=Poiret+One&display=swap">
<style>
  :root {
    --page: #ffffff;
    --card: #000000;
    --frame: #8a8a8a;
    --silver: #d9d9d9;
    --silver-light: #f2f2f2;
    --silver-dark: #6e6e6e;
  }
  html, body {
    margin: 0;
    width: 1200px;
    height: 800px;
    overflow: hidden;
    background: var(--page);
  }
  .card {
    position: absolute;
    left: 50px;
    top: 48px;
    width: 1110px;
    height: 704px;
    background: var(--card);
    box-shadow: 0 0 0 2px #333;
  }
  .card__frame {
    position: absolute;
    left: 0;
    top: 0;
  }
  .corner-ornament {
    position: absolute;
    width: 120px;
    height: 100px;
    background: radial-gradient(circle at 20% 20%, var(--silver-light), var(--silver-dark) 40%, transparent 65%);
    opacity: 0.85;
  }
  .corner-ornament--tl { left: 14px; top: 10px; }
  .corner-ornament--tr { right: 14px; top: 10px; transform: scaleX(-1); }
  .corner-ornament--bl { left: 14px; bottom: 10px; transform: scaleY(-1); }
  .corner-ornament--br { right: 14px; bottom: 10px; transform: scale(-1, -1); }
  .card__title {
    position: absolute;
    left: 0;
    right: 0;
    top: 232px;
    margin: 0;
    text-align: center;
    font-family: "Pirata One", cursive;
    font-weight: 400;
    font-size: 46px;
    line-height: 1.2;
    letter-spacing: 1px;
    color: var(--silver);
    text-shadow: 0 1px 0 var(--silver-light), 0 -1px 0 var(--silver-dark);
  }
  .emblem {
    position: absolute;
    left: 340px;
    top: 314px;
    width: 415px;
    height: 198px;
    background: linear-gradient(180deg, #bdbdbd 0%, #8c8c8c 50%, #4a4a4a 100%);
    clip-path: polygon(0 30%, 40% 15%, 50% 0, 60% 15%, 100% 30%, 88% 70%, 60% 80%, 50% 100%, 40% 80%, 12% 70%);
  }
  .contact {
    position: absolute;
    left: 118px;
    top: 606px;
    margin: 0;
    display: flex;
    align-items: baseline;
    gap: 14px;
    font-family: "Poiret One", sans-serif;
    font-size: 34px;
    line-height: 1.2;
    color: var(--silver);
    white-space: nowrap;
  }
  .contact__web { font-size: 29px; }
  .social {
    position: absolute;
    left: 902px;
    top: 614px;
    display: flex;
    align-items: center;
    gap: 6px;
    font-family: "Poiret One", sans-serif;
    font-size: 20px;
    line-height: 1.2;
    color: var(--silver);
    white-space: nowrap;
  }
  .social__mark {
    width: 14px;
    height: 14px;
    background: var(--silver);
  }
</style>
</head>
<body>
  <section class="card">
    <svg class="card__frame" width="1110" height="704" viewBox="0 0 1110 704" aria-hidden="true">
      <rect x="20" y="20" width="1070" height="664" fill="none" stroke="var(--frame)" stroke-width="2"/>
      <rect x="26" y="26" width="1058" height="652" fill="none" stroke="#444" stroke-width="1"/>
    </svg>

    <div class="corner-ornament corner-ornament--tl" role="img" aria-label="Silver scrollwork corner ornament"></div>
    <div class="corner-ornament corner-ornament--tr" role="img" aria-label="Silver scrollwork corner ornament"></div>
    <div class="corner-ornament corner-ornament--bl" role="img" aria-label="Silver scrollwork corner ornament"></div>
    <div class="corner-ornament corner-ornament--br" role="img" aria-label="Silver scrollwork corner ornament"></div>

    <h1 class="card__title">Marlowe Hairdressing &amp; The Willowmere Beauty</h1>

    <div class="emblem" role="img" aria-label="Ornate silver winged crest emblem"></div>

    <p class="contact">
      <span class="contact__tel">Tel 01632 418550</span>
      <span class="contact__web">www.marlowehairdressing.example.co.uk</span>
    </p>

    <div class="social">
      <span class="social__mark" aria-hidden="true"></span>
      <span class="social__name">chatterbook</span>
    </div>
  </section>
</body>
</html>
```